Business Card Design Project

I need a new business card design for my Remodel/Design/Build company, Brightfield Renovation Works, Inc. See our website: www.brightfieldrenovationworks.com
We are an established company with a growing reputation and growing quickly. We are know for being on the forward edge of the industry, producing a great product and our "people friendly" approach.
I am looking for something cool, transitional, maybe even retro that captures the imagination, shows our sleek creativity and streamlined approach as well as communicates stability and trustworthiness.
Updates

Stainless steel business card design would be cool.

Please have all future designs with full logo colors and shown on a stainless steel business card.  Also, logo and tag line will most likely be printed with spot uv, so layers will be necessary.  Thank you.

Target Market(s)

30-65 yrs old, homeowners, appreciate fine things, median income $150+k, net worth $1+m

Industry/Entity Type

Business

Requirements
Must have
• Company Logo
Contact information
Website URL
Nice to have
• Tagline: Building Relationships and Remodeling Homes...One Client at a Time.
Double-sided okay.
Stainless steel business card.

```html
<!DOCTYPE html>
<html lang="en">
<head>
<meta charset="utf-8">
<title>Brightfield Renovation Works – Business Card</title>
<link rel="stylesheet" href="https://fonts.googleapis.com/css2?family=Michroma&family=Open+Sans:wght@400;600&display=swap">
<style>
  :root {
    --backdrop: #d4d6d8;
    --card-dark: #0b0c0e;
    --card-mid: #1c1e22;
    --tile: rgba(255,255,255,0.035);
    --brand-red: #a3161b;
    --phone-red: #b3252a;
    --url-grey: #9c9ea2;
    --mark-grey: #3a3c40;
    --mark-edge: #8d9095;
  }
  html, body {
    margin: 0;
    padding: 0;
    width: 1200px;
    height: 952px;
    overflow: hidden;
    background: var(--backdrop);
  }
  .business-card {
    position: absolute;
    left: 100px;
    top: 190px;
    width: 1000px;
    height: 571px;
    border-radius: 6px;
    overflow: hidden;
    background: linear-gradient(160deg, var(--card-mid) 0%, var(--card-dark) 55%, #050506 100%);
    box-shadow: 0 10px 30px rgba(0,0,0,0.25);
  }
  .tile-pattern {
    position: absolute;
    inset: 0;
  }
  .brand-lockup {
    position: absolute;
    left: 70px;
    top: 150px;
    display: flex;
    align-items: center;
    gap: 22px;
  }
  .brand-dot {
    width: 64px;
    height: 64px;
    border-radius: 50%;
    background: var(--brand-red);
    flex: none;
  }
  .brand-name {
    margin: 0;
    font-family: "Michroma", sans-serif;
    font-weight: 400;
    font-size: 25px;
    line-height: 1.35;
    letter-spacing: 1px;
    text-transform: uppercase;
    color: var(--brand-red);
  }
  .brand-mark-area {
    position: absolute;
    right: 70px;
    top: 60px;
    width: 330px;
    height: 330px;
    border-radius: 50%;
    background: radial-gradient(circle at 40% 35%, #4a4c51 0%, var(--mark-grey) 60%, #26282b 100%);
    border: 10px solid var(--mark-edge);
    box-sizing: border-box;
  }
  .contact {
    position: absolute;
    left: 70px;
    bottom: 60px;
    font-family: "Open Sans", sans-serif;
  }
  .contact-phone {
    margin: 0 0 6px;
    font-size: 34px;
    font-weight: 400;
    color: var(--phone-red);
  }
  .contact-url {
    margin: 0;
    font-size: 24px;
    font-weight: 400;
    color: var(--url-grey);
  }
</style>
</head>
<body>
  <section class="business-card">
    <svg class="tile-pattern" width="1000" height="571" viewBox="0 0 1000 571" aria-hidden="true">
      <rect x="40" y="30" width="180" height="90" fill="var(--tile)"/>
      <rect x="260" y="70" width="140" height="120" fill="var(--tile)"/>
      <rect x="120" y="230" width="220" height="70" fill="var(--tile)"/>
      <rect x="420" y="20" width="120" height="110" fill="var(--tile)"/>
      <rect x="380" y="260" width="160" height="90" fill="var(--tile)"/>
      <rect x="200" y="360" width="150" height="80" fill="var(--tile)"/>
      <rect x="560" y="380" width="130" height="100" fill="var(--tile)"/>
    </svg>

    <div class="brand-lockup">
      <span class="brand-dot"></span>
      <h1 class="brand-name">Brightfield<br>Renovation Works</h1>
    </div>

    <div class="brand-mark-area" role="img" aria-label="Large brand mark emblem area"></div>

    <div class="contact">
      <p class="contact-phone">(555) 214-7380</p>
      <p class="contact-url">www.brightfieldrenovationworks.com</p>
    </div>
  </section>
</body>
</html>
```